plumvantage.com design project

We need a wordpress design for a new company called plumvantage. We are a social networking site for poker players. We are an affiliate company for both poker sites and poker products. We want a friendly and welcoming scheme. We are thinking we want a blue color scheme.
Updates

Reason: We extended the deadline because we are having a logo designed as well.

We have decided to extend the deadline because we are getting a logo designed. We have also decided to commit to the designer payments.

It would be most helpful to see a design for both the homepage and social networking profile page if possible. Thanks. 

Could you guys please incorporate this logo into the some of the designs. It is the best logo we have received so far.

http://files.examplehost-gallery.net/img/40213/8817/8817_2246091_40213_image.jpg

Another website we really like the background on is www.foldtwice.net . We are open to the idea that the color scheme doesn't have to necessarily be blue but we do want something that is easy on the eyes. We don't want a site that looks super "busy" but easily navigable at the same time professional and welcoming. Thank you!

Target Market(s)

Poker players, mostly males aged 18-30

Industry/Entity Type

It Company

Requirements
Must have
• -We need a social networking feature with the ability for customers to create and modify a profile page.
-A nicely designed forum.
-A menu bar with customizable tabs.
-Easy for us to add information/pages/blog posts to site.
Nice to have
• -Ability for users to upload videos and photos.
-Ability for users chat with one another.

```html
<!DOCTYPE html>
<html lang="en">
<head>
<meta charset="utf-8">
<title>plumvantage — Poker Social Network</title>
<link href="https://fonts.googleapis.com/css2?family=PT+Sans:wght@400;700&family=Arimo:wght@400;700&display=swap" rel="stylesheet">
<style>
:root{
  --header-top:#2ea8b8;
  --header-mid:#1a5a82;
  --header-deep:#123a5e;
  --nav-active:#2b9aa6;
  --footer:#1d3f62;
  --footer-bar:#142d47;
  --link:#1d6b8c;
  --ink:#222;
  --body:#333;
  --muted:#666;
  --panel:#f3f3f3;
  --panel-line:#dedede;
  --white:#fff;
  --btn:#1f4f77;
}
*{box-sizing:border-box;margin:0;padding:0}
html,body{width:882px;height:1200px;overflow:hidden;background:var(--white)}
body{position:relative;font-family:"Arimo",Arial,sans-serif;color:var(--body)}
.abs{position:absolute}
.heading{font-family:"PT Sans",sans-serif;color:var(--ink)}

/* header */
.site-header{left:0;top:0;width:882px;height:108px;background:linear-gradient(180deg,var(--header-top) 0%,var(--header-mid) 48%,var(--header-deep) 68%,var(--header-deep) 100%)}
.site-header::after{content:"";position:absolute;left:0;right:0;bottom:0;height:4px;background:var(--nav-active)}
.brand{left:92px;top:14px;font-family:"PT Sans",sans-serif;font-size:36px;color:var(--white);letter-spacing:-.5px}
.top-links{right:75px;top:8px;display:flex;gap:20px;font-size:10px;color:var(--white)}
.search{left:638px;top:43px;width:158px;height:21px;background:var(--white);border-radius:3px;font-size:10px;color:#999;padding:4px 5px}
.search svg{position:absolute;right:5px;top:3px}
.main-nav{left:77px;top:77px;display:flex;font-family:"PT Sans",sans-serif;font-size:12.5px;color:var(--white)}
.main-nav span{padding:5px 10px 10px;margin-right:2px}
.main-nav .active{background:var(--nav-active);border-radius:3px 3px 0 0}

/* hero + login */
.hero{left:75px;top:125px;width:520px;height:181px;background:#ddd;padding:4px}
.hero div{width:100%;height:100%;background:linear-gradient(90deg,#e8e4df 0%,#3a2f2a 40%,#1b3b5c 60%,#6a8fb8 80%,#1a1f33 100%)}
.signin{left:608px;top:124px;width:192px;height:182px;background:linear-gradient(180deg,#fafafa,#e6e6e6);border:1px solid #e0e0e0;padding:4px 10px}
.signin h2{font-size:18px;font-weight:400;margin-bottom:10px}
.signin label{display:block;font-size:10px;font-weight:700;color:#333;margin-bottom:3px}
.signin .field{width:158px;height:18px;background:var(--white);border:1px solid #ddd;margin-bottom:8px}
.signin .row{display:flex;align-items:center;justify-content:space-between;width:158px;font-size:9px}
.signin .box{width:9px;height:9px;border:1px solid #999;display:inline-block;margin-right:4px;vertical-align:middle}
.btn{background:var(--btn);color:var(--white);font-size:10.5px;padding:4px 13px;border-radius:3px}

/* welcome */
.welcome-title{left:78px;top:327px;font-size:21px}
.date{right:97px;top:350px;font-size:9px;font-weight:700;color:#222}
.welcome-img{left:83px;top:367px;width:221px;height:109px;border:1px solid #ddd;background:linear-gradient(90deg,#f2f4f6,#b9c2cc 50%,#5b4a44 80%,#eef0f2)}
.welcome-text{left:313px;top:368px;width:475px;font-size:9px;line-height:14.7px;color:#333}
.welcome-text p{margin-bottom:8px}

/* sections */
.panel{background:var(--panel);border:1px solid var(--panel-line)}
.social{left:76px;top:506px;width:516px;height:286px}
.section-title{font-size:19px;font-weight:400;position:absolute;left:3px;top:2px}
.feature{position:absolute;top:42px;width:135px}
.feature .thumb{width:128px;height:96px;border:5px solid #ccc;background:var(--white);display:flex;align-items:center;justify-content:center}
.feature p{margin-top:14px;font-size:9px;line-height:13.2px;color:#333}
.divider{position:absolute;top:44px;width:1px;height:226px;background:#ddd}

.members{left:601px;top:506px;width:191px;height:286px}
.members h3{font-size:16.5px;font-weight:400;padding:5px 16px;background:linear-gradient(180deg,#fff,#efefef)}
.member{display:flex;align-items:center;margin:0 0 4px 8px;height:36px}
.avatar{width:36px;height:36px;margin-right:8px}
.member b{display:block;font-family:"PT Sans",sans-serif;font-size:10.5px;color:var(--link)}
.member small{font-family:"PT Sans",sans-serif;font-size:8.5px;font-weight:700;color:#555}

.blogs{left:75px;top:818px;width:515px;height:181px}
.blog{position:absolute;left:6px;width:480px}
.blog .pic{position:absolute;left:0;top:0;width:36px;height:36px;background:#eee;border:1px solid #ddd}
.blog h4{margin-left:42px;font-size:13.5px;color:var(--link)}
.blog .meta{margin-left:43px;font-size:7.5px;color:#666}
.blog p{margin-left:44px;font-size:8.5px;line-height:10.5px;color:#555;margin-top:3px}
.blog-sep{position:absolute;left:6px;top:107px;width:477px;height:1px;background:#ddd}

.video{left:603px;top:818px;width:197px;height:180px;background:radial-gradient(circle at 50% 45%,#333,#0c0c0c 70%)}
.video .bar{position:absolute;left:7px;bottom:6px;width:185px;height:12px;background:#d9d9d9;display:flex;align-items:center;font-size:6px;color:#222;gap:4px;padding:0 4px}
.video .track{flex:1;height:3px;background:#999}

/* footer */
.site-footer{left:0;top:1027px;width:882px;height:150px;background:var(--footer)}
.foot-col{position:absolute;top:13px;color:var(--white)}
.foot-col h5{font-family:"PT Sans",sans-serif;font-size:14.5px;font-weight:400;margin-bottom:10px}
.foot-col li{list-style:none;font-size:9.5px;line-height:16.2px;padding-left:9px;position:relative}
.foot-col li::before{content:"";position:absolute;left:0;top:6px;border-left:3px solid #8fa6bd;border-top:2.5px solid transparent;border-bottom:2.5px solid transparent}
.socials{left:631px;top:19px;display:flex;gap:5px}
.socials span{width:33px;height:33px;background:#3a668f;border-radius:2px}
.foot-brand{left:604px;top:78px;font-family:"PT Sans",sans-serif;font-size:33px;color:#dfe6ee}
.copyright{left:0;top:1177px;width:882px;height:23px;background:var(--footer-bar);color:var(--white);font-size:9.5px;text-align:center;line-height:23px}
</style>
</head>
<body>

<header class="site-header abs">
  <div class="brand abs">plumvantage</div>
  <nav class="top-links abs"><span>plumvantageforum</span><span>Promotions</span><span>Contact</span><span>Log in</span><span>Register</span></nav>
  <div class="search abs">Search...
    <svg width="14" height="14" viewBox="0 0 14 14"><circle cx="5.5" cy="5.5" r="4" fill="none" stroke="#222" stroke-width="1.8"/><line x1="8.5" y1="8.5" x2="13" y2="13" stroke="#222" stroke-width="2"/></svg>
  </div>
  <nav class="main-nav abs">
    <span class="active">Best Rakeback Deals</span><span>Table Talk</span><span>plumvantage Community</span><span>Online Poker Rooms</span><span>Live Poker Rooms</span><span>Poker Tools and Resources</span>
  </nav>
</header>

<section class="hero abs"><div role="img" aria-label="Banner photo of a poker player with cards and chips beside a glowing online poker sites graphic"></div></section>

<aside class="signin abs">
  <h2 class="heading">Sign In or Join</h2>
  <label>Username</label><div class="field"></div>
  <label>Password</label><div class="field"></div>
  <div class="row"><span><i class="box"></i>Remember Me</span><span class="btn">Sign In</span></div>
</aside>

<h1 class="welcome-title heading abs" style="font-weight:400">Welcome to plumvantage</h1>
<div class="date abs">November 25, 2012</div>
<div class="welcome-img abs" role="img" aria-label="Photo of a businesswoman sketching sharing arrows on a glass board"></div>
<div class="welcome-text abs">
  <p>The goal at plumvantage is to create an environment for both poker players and poker rooms to prosper and grow the poker community as a whole. We are currently in the process of designing and creating features to help poker players. We highly value poker players' input poker players and poker rooms to prosper and grow the poker community as a whole. We are currently in poker players and poker rooms to prosper and grow the poker community as a whole.</p>
  <p>We are currently in poker players and poker rooms to prosper and grow the poker community as a whole. We are currently inand would greatly appreciate any feedback on issues or services that players would like to see offered.</p>
</div>

<section class="social panel abs">
  <h2 class="section-title heading">Social Networking</h2>
  <div class="feature" style="left:6px">
    <div class="thumb" role="img" aria-label="Illustration of a colourful network of people">
      <svg width="96" height="80" viewBox="0 0 96 80"><g stroke="#999" stroke-width="1"><line x1="48" y1="30" x2="20" y2="50"/><line x1="48" y1="30" x2="76" y2="20"/><line x1="48" y1="30" x2="70" y2="60"/><line x1="48" y1="30" x2="28" y2="18"/></g><circle cx="48" cy="30" r="9" fill="#f5b800"/><circle cx="20" cy="52" r="9" fill="#f07a20"/><circle cx="70" cy="62" r="8" fill="#e0287a"/><circle cx="76" cy="20" r="6" fill="#3aa0e0"/><circle cx="28" cy="18" r="6" fill="#6cc04a"/></svg>
    </div>
    <p>He starts off his presentation with the quote above and goes on to illustrate how the <b>game of poker forces players</b> to continually question the validity of their own beliefs. Few people are reminded more frequently than poker players how little they know.</p>
  </div>
  <div class="divider" style="left:162px"></div>
  <div class="feature" style="left:188px">
    <div class="thumb" role="img" aria-label="Illustration of a profile card with a padlock">
      <svg width="80" height="70" viewBox="0 0 80 70"><rect x="6" y="8" width="54" height="50" rx="3" fill="#4fb3d9"/><rect x="44" y="36" width="28" height="24" rx="4" fill="#aab4bd"/><path d="M49 36v-8a9 9 0 0 1 18 0v8" fill="none" stroke="#8a949d" stroke-width="4"/></svg>
    </div>
    <p>He starts off his presentation with the quote above and goes on to illustrate how the <b>game of poker forces players</b> to continually question the validity of their own beliefs. Few people are reminded more frequently than poker players how little they know.</p>
  </div>
  <div class="divider" style="left:338px"></div>
  <div class="feature" style="left:360px">
    <div class="thumb" role="img" aria-label="Illustration of a red gift box with a blue ribbon">
      <svg width="70" height="74" viewBox="0 0 70 74"><rect x="10" y="26" width="50" height="44" fill="#d01f1f"/><rect x="6" y="18" width="58" height="12" fill="#e23030"/><rect x="31" y="18" width="8" height="52" fill="#9ccfd8"/></svg>
    </div>
    <p>He starts off his presentation with the quote above and goes on to illustrate how the <b>game of poker forces players</b> to continually question the validity of their own beliefs. Few people are reminded more frequently than poker players how little they know.</p>
  </div>
</section>

<aside class="members panel abs">
  <h3 class="heading">Popular Members</h3>
  <div style="margin-top:8px">
    <div class="member"><div class="avatar" role="img" aria-label="Member photo" style="background:#5b5347"></div><div><b>Marco Delaney</b><small>2,413 friends</small></div></div>
    <div class="member"><div class="avatar" role="img" aria-label="Member avatar" style="background:#3f9a4a;border-radius:50%"></div><div><b>ChipShotPics</b><small>903 friends</small></div></div>
    <div class="member"><div class="avatar" role="img" aria-label="Member photo" style="background:#8a6a3c"></div><div><b>Gavin Ashford</b><small>789 friends</small></div></div>
    <div class="member"><div class="avatar" role="img" aria-label="Member photo" style="background:#8a8f9a"></div><div><b>Owen Reyes</b><small>582 friends</small></div></div>
    <div class="member"><div class="avatar" role="img" aria-label="Member photo" style="background:#4a4a55"></div><div><b>Clay Rowan</b><small>566 friends</small></div></div>
    <div class="member"><div class="avatar" role="img" aria-label="Member avatar" style="background:#b8262a"></div><div><b>riverhog</b><small>532 friends</small></div></div>
  </div>
</aside>

<section class="blogs panel abs">
  <h2 class="section-title heading" style="left:9px">Lastest Blogs</h2>
  <article class="blog" style="top:38px">
    <div class="pic" role="img" aria-label="Author avatar placeholder"></div>
    <h4>Game of poker forces players</h4>
    <div class="meta">Posted October 17, 2012</div>
    <p>He starts off his presentation with the quote above and goes on to illustrate how the game of poker forces players to continually question the validity of their own beliefs. Few people are reminded more frequently than poker players how little they know.</p>
  </article>
  <div class="blog-sep"></div>
  <article class="blog" style="top:117px">
    <div class="pic" role="img" aria-label="Author avatar placeholder"></div>
    <h4>Game of poker forces players</h4>
    <div class="meta">Posted September 13, 2012 by</div>
    <p>He starts off his presentation with the quote above and goes on to illustrate how the game of poker forces players to continually question the validity of their own beliefs.</p>
  </article>
</section>

<div class="video abs" role="img" aria-label="Embedded video player">
  <svg class="abs" style="left:78px;top:66px" width="44" height="32" viewBox="0 0 44 32"><rect width="44" height="32" rx="2" fill="#888"/><polygon points="17,8 17,24 30,16" fill="#111"/></svg>
  <div class="bar"><span>▶</span><span>00:00</span><span class="track"></span><span>00:00</span></div>
</div>

<footer class="site-footer abs">
  <div class="foot-col" style="left:104px"><h5>Pokar Player</h5><ul><li>Business Websites</li><li>Reviews</li><li>Quick Tour</li><li>Pricing</li><li>Free Trial</li></ul></div>
  <div class="foot-col" style="left:251px"><h5>Pokar Player</h5><ul><li>Marketing Tips</li><li>Search Optimisation</li><li>Social Media</li><li>Video Marketing</li><li>Business Cases</li></ul></div>
  <div class="foot-col" style="left:413px"><h5>Pokar Player</h5><ul><li>Help/Contact us</li><li>Business directory</li><li>Legal notices</li><li>Privacy policy</li><li>Terms &amp; Conditions</li></ul></div>
  <div class="socials abs" aria-label="Social links"><span></span><span></span><span></span><span></span></div>
  <div class="foot-brand abs">plumvantage</div>
</footer>
<div class="copyright abs">Copyright © 2012 plumvantage. All Rights Reserved.</div>

</body>
</html>
```